Stationery Design Project

Need stationery based on logo

Stationery should include:

Letterhead-should include logo at the top, and contact info at the bottom
Envelope should include mailing address  at top left corner (Corvath Tutoring Services, 4867 Brisk...)
PPT slide should include Logo only
Cover page should just include logo

Requirements
Must have
• Based on logo

```html
<!DOCTYPE html>
<html lang="en">
<head>
<meta charset="utf-8">
<title>Corvath Tutoring Stationery</title>
<link rel="stylesheet" href="https://fonts.googleapis.com/css2?family=EB+Garamond:wght@400;600&display=swap">
<style>
  :root{
    --backdrop:#f1f1f1;
    --paper:#ffffff;
    --gold:#d7a444;
    --ink:#3b3b3b;
    --muted:#a9a9a9;
    --rule:#c9c9c9;
    --serif:"EB Garamond", Georgia, serif;
  }
  *{margin:0;padding:0;box-sizing:border-box}
  html,body{width:1200px;height:1000px;overflow:hidden}
  body{background:var(--backdrop);font-family:var(--serif);position:relative}
  .sheet{position:absolute;background:var(--paper);box-shadow:6px 10px 22px rgba(0,0,0,.16);overflow:hidden}
  .letterhead{left:67px;top:31px;width:378px;height:534px}
  .cover{left:542px;top:30px;width:371px;height:524px}
  .card-front{left:940px;top:33px;width:242px;height:155px}
  .card-back{left:940px;top:237px;width:242px;height:155px}
  .slide{left:67px;top:617px;width:425px;height:318px}
  .envelope{left:546px;top:617px;width:405px;height:203px}

  .wordmark{position:absolute;color:var(--ink);font-weight:400;letter-spacing:.12em;white-space:nowrap;line-height:1;display:flex;align-items:center;gap:.4em}
  .wordmark .dot{width:.5em;height:.5em;border-radius:50%;background:var(--gold);flex:none}
  .wordmark.center{left:0;right:0;justify-content:center}

  .band{position:absolute;background:var(--gold)}
  .rule{position:absolute;height:1px;background:var(--rule)}

  .contact{position:absolute;text-align:center;font-size:5px;line-height:1.35;color:var(--muted)}
  .contact .org{color:var(--gold);font-weight:600}

  .cover-info{position:absolute;left:0;right:0;top:274px;text-align:center;font-size:7.5px;line-height:1.5;color:#222}
  .cover-info .person{font-weight:600;margin-bottom:14px}

  .card-person{position:absolute;left:0;right:0;top:119px;text-align:center;font-size:7.5px;line-height:1.7;color:#222}
  .card-person .name{font-weight:600}

  .bullets{position:absolute;left:21px;top:72px;list-style:none}
  .bullets li{width:8px;height:8px;border-radius:50%;background:var(--gold);margin-bottom:25px}
  .slide-text{position:absolute;left:65px;top:152px;font-size:24px;color:var(--muted);letter-spacing:.01em}

  .return-address{position:absolute;left:14px;top:10px;font-size:6px;line-height:1.35;color:var(--muted)}
  .return-address .org{color:var(--gold);font-weight:600}
</style>
</head>
<body>

<section class="sheet letterhead" aria-label="Letterhead">
  <div class="wordmark" style="left:15px;top:38px;font-size:12px"><span class="dot"></span>CORVATH TUTORING</div>
  <div class="band" style="left:15px;top:50px;width:349px;height:8px"></div>
  <div class="rule" style="left:10px;right:11px;top:491px"></div>
  <address class="contact" style="left:0;right:0;top:497px;font-style:normal">
    <div class="org">Corvath Tutoring Services</div>
    <div>4867 Brisk Lane</div>
    <div>Alder CA, 95420</div>
    <div>555-014-2271</div>
    <div>www.corvathtutoring.com</div>
  </address>
</section>

<section class="sheet cover" aria-label="Cover page">
  <div class="wordmark center" style="top:200px;font-size:20px"><span class="dot"></span>CORVATH TUTORING</div>
  <div class="band" style="left:60px;top:226px;width:251px;height:10px"></div>
  <div class="cover-info">
    <div class="person">Helen Marsh</div>
    <div>Cover Page Sample</div>
    <div>Corvath Tutoring Services</div>
    <div>23/01/13</div>
  </div>
  <div class="rule" style="left:9px;right:11px;top:496px"></div>
</section>

<section class="sheet card-front" aria-label="Business card front">
  <div class="wordmark center" style="top:84px;font-size:13px"><span class="dot"></span>CORVATH TUTORING</div>
  <div class="band" style="left:50px;top:99px;width:142px;height:6px"></div>
  <div class="card-person">
    <div class="name">Helen Marsh</div>
    <div>Principal</div>
  </div>
</section>

<section class="sheet card-back" aria-label="Business card back">
  <address class="contact" style="left:0;right:0;top:72px;font-size:6.5px;font-style:normal">
    <div class="org">Corvath Tutoring Services</div>
    <div>4867 Brisk Lane</div>
    <div>Alder CA, 95420</div>
    <div>555-014-2271</div>
    <div>hm@corvathtutoring.com</div>
  </address>
</section>

<section class="sheet slide" aria-label="Presentation slide">
  <div class="wordmark" style="left:15px;top:30px;font-size:12px"><span class="dot"></span>CORVATH TUTORING</div>
  <div class="band" style="left:15px;top:45px;width:393px;height:7px"></div>
  <ul class="bullets"><li></li><li></li><li></li><li></li><li></li><li></li><li></li></ul>
  <div class="slide-text">POWERPOINT SLIDE TEXT</div>
</section>

<section class="sheet envelope" aria-label="Envelope">
  <address class="return-address" style="font-style:normal">
    <div class="org">Corvath Tutoring Services</div>
    <div>4867 Brisk Lane</div>
    <div>Alder CA, 95420</div>
    <div>555-014-2271</div>
    <div>www.corvathtutoring.com</div>
  </address>
</section>

</body>
</html>
```